Business Card New Design for Corvella

We would like a new look on our business card, using the same style, the same colors blue, gray and white with similar font that is represented on the new Sell Sheet. We recently re-designed our Sell Sheets - I've attached a sell sheet file for your reference. I've also attached our current business card and our logo. Keep the same information listed on each side of the card.

Contact Information for Business Card

Use details given on example provided

Font styles to use
Other font styles liked:
• Myriad Regular and Bold

Colors

Designer to choose colors to be used in the design.

Requirements
Must have
• Current Information that was provided on the current business card. Colors Must use Blue, Gray and White, the same colors as the sell sheet example.

```html
<!DOCTYPE html>
<html lang="en">
<head>
<meta charset="utf-8">
<title>Corvella Business Card</title>
<link rel="stylesheet" href="https://fonts.googleapis.com/css2?family=Source+Sans+3:wght@400;600;700&display=swap">
<style>
  :root {
    --stage: #b9b9b9;
    --brand-blue: #3340a3;
    --brand-blue-dark: #2a3590;
    --ink-gray: #4a4a4a;
    --soft-gray: #6b6b6b;
    --paper: #ffffff;
  }
  * { margin: 0; padding: 0; box-sizing: border-box; }
  html, body { width: 1200px; height: 930px; overflow: hidden; }
  body {
    background: radial-gradient(ellipse at 50% 40%, #d2d2d2, var(--stage) 75%);
    font-family: "Source Sans 3", "Myriad Pro", sans-serif;
    position: relative;
  }
  .card {
    position: absolute;
    width: 580px;
    height: 331px;
    border-radius: 22px;
    overflow: hidden;
    box-shadow: 0 8px 22px rgba(0,0,0,.25);
  }
  /* front */
  .card-front {
    left: 60px; top: 70px;
    background: linear-gradient(135deg, #3a48b0, var(--brand-blue-dark));
    color: var(--paper);
  }
  .brand-name {
    font-weight: 700;
    letter-spacing: 6px;
    text-transform: uppercase;
  }
  .card-front .brand-name {
    position: absolute; left: 0; right: 0; top: 58px;
    text-align: center; font-size: 52px; color: var(--paper);
  }
  .card-front .divider {
    position: absolute; left: 40px; right: 40px; top: 150px;
    height: 1px; background: rgba(255,255,255,.8);
  }
  .service-list {
    position: absolute; list-style: none;
    font-size: 16px; line-height: 23px;
  }
  .service-list li { padding-left: 20px; position: relative; }
  .service-list li::before {
    content: ""; position: absolute; left: 2px; top: 8px;
    width: 8px; height: 8px; border-radius: 50%; background: var(--paper);
  }
  .services-primary { left: 40px; top: 182px; }
  .services-secondary { left: 320px; top: 182px; }

  /* back */
  .card-back {
    left: 560px; top: 530px;
    background: var(--paper);
    color: var(--ink-gray);
  }
  .card-back .brand-name {
    position: absolute; left: 36px; top: 40px;
    font-size: 34px; color: var(--brand-blue); letter-spacing: 4px;
  }
  .holder {
    position: absolute; right: 40px; top: 52px; text-align: right;
  }
  .holder-name {
    font-size: 30px; font-weight: 700; color: var(--brand-blue);
    letter-spacing: .5px; line-height: 1;
  }
  .holder-title { font-size: 17px; color: var(--soft-gray); margin-top: 2px; }
  .accent-bar {
    position: absolute; right: 0; top: 50px; width: 10px; height: 40px;
    background: var(--brand-blue);
  }
  .card-back .divider {
    position: absolute; left: 36px; right: 40px; top: 128px;
    height: 1.5px; background: var(--brand-blue);
  }
  .address {
    position: absolute; left: 36px; bottom: 34px;
    font-size: 17px; line-height: 22px; color: var(--ink-gray);
  }
  .address .line { display: flex; align-items: center; gap: 8px; }
  .address .plain { padding-left: 0; }
  .phones {
    position: absolute; right: 40px; top: 146px;
    font-size: 17px; line-height: 23px; text-align: right; color: var(--ink-gray);
  }
  .phones .line { display: flex; justify-content: flex-end; align-items: center; gap: 8px; }
  .icon { width: 13px; height: 13px; fill: none; stroke: var(--brand-blue); stroke-width: 1.6; flex-shrink: 0; }
  .icon-spacer { width: 13px; }
</style>
</head>
<body>

<section class="card card-front" aria-label="Card front">
  <div class="brand-name">Corvella</div>
  <div class="divider"></div>
  <ul class="service-list services-primary">
    <li>Conveyyors</li>
    <li>Target Sauce Applicators</li>
    <li>TargerTopping Applicators</li>
    <li>Waterfall Toppng Applicators</li>
    <li>Pepeeroni / Meat Sliger / Applicators</li>
  </ul>
  <ul class="service-list services-secondary">
    <li>Portion Controlled Filler Pimps</li>
    <li>Dry Ingredient Applicators</li>
    <li>Check Weigh Conveyors</li>
    <li>Portion Compensators</li>
  </ul>
</section>

<section class="card card-back" aria-label="Card back">
  <div class="brand-name">Corvella</div>
  <div class="accent-bar"></div>
  <div class="holder">
    <div class="holder-name">MARTIN HALE</div>
    <div class="holder-title">CEO</div>
  </div>
  <div class="divider"></div>

  <div class="phones">
    <div class="line">(555) 310-2746
      <svg class="icon" viewBox="0 0 16 16"><path d="M3 2l3 0 1 3-2 1.5c1 2 2.5 3.5 4.5 4.5L11 9l3 1v3c-6 1-12-5-11-11z"/></svg>
    </div>
    <div class="line">(555) 310-8812
      <svg class="icon" viewBox="0 0 16 16"><rect x="4" y="1.5" width="8" height="13" rx="1.5"/><path d="M7 12h2"/></svg>
    </div>
    <div class="line">(555) 627-4093
      <svg class="icon" viewBox="0 0 16 16"><rect x="2" y="7" width="12" height="7" rx="1"/><path d="M4 7V2h8v5M5 10h6"/></svg>
    </div>
    <div class="line">(800) 555-0147 x 226 Toll Free
      <svg class="icon" viewBox="0 0 16 16"><path d="M3 2l3 0 1 3-2 1.5c1 2 2.5 3.5 4.5 4.5L11 9l3 1v3c-6 1-12-5-11-11z"/></svg>
    </div>
  </div>

  <div class="address">
    <div class="line">4180 Harborline road</div>
    <div class="line">millbrook, IL 60499</div>
    <div class="line">
      <svg class="icon" viewBox="0 0 16 16"><rect x="1.5" y="3.5" width="13" height="9" rx="1"/><path d="M1.5 4l6.5 5 6.5-5"/></svg>
      mhale@c-t-s.com
    </div>
    <div class="line">
      <svg class="icon" viewBox="0 0 16 16"><circle cx="8" cy="8" r="6.5"/><path d="M1.5 8h13M8 1.5c-3 3.5-3 9.5 0 13M8 1.5c3 3.5 3 9.5 0 13"/></svg>
      www.c-t-s.com
    </div>
  </div>
</section>

</body>
</html>
```